study by ripples circle

The website presents a new interactive learning system where it provides not only the teaching material as the instructor friend who can both teach and learn, making friends and making money.
Make friends and get money.

```html
<!DOCTYPE html>
<html lang="en">
<head>
<meta charset="utf-8">
<title>Ripples — study by ripples circle</title>
<link rel="stylesheet" href="https://fonts.googleapis.com/css2?family=Open+Sans:wght@400;600;700;800&display=swap">
<style>
:root{
  --navy:#0b1a2e;
  --navy-2:#10243f;
  --hero-a:#0d3a6b;
  --hero-b:#061a33;
  --blue:#1b8fd6;
  --blue-dark:#1572b4;
  --ink:#333b45;
  --muted:#7b8590;
  --line:#e3e7eb;
  --paper:#ffffff;
  --panel:#f4f6f8;
  --green:#2ecc71;
  --login-l:#222a33;
  --foot:#1e2125;
  --foot-2:#15171a;
  --foot-text:#a9b0b7;
}
*{box-sizing:border-box;margin:0;padding:0}
html,body{width:678px;height:1200px;overflow:hidden}
body{font-family:"Open Sans",sans-serif;color:var(--ink);background:var(--paper);font-size:9px;line-height:1.5}
.site{width:678px;height:1200px;position:relative}

/* header */
.topbar{height:40px;background:var(--navy);display:flex;align-items:center;justify-content:space-between;padding:0 24px 0 70px}
.brand{display:flex;align-items:center;gap:7px;color:#fff;font-weight:800;font-size:17px;letter-spacing:1px}
.brand-dot{width:11px;height:11px;border-radius:50%;background:var(--blue)}
.nav{display:flex;gap:20px;list-style:none}
.nav li{color:#aebbc9;font-size:7px;font-weight:600;text-transform:uppercase}
.nav li.active{color:#fff;border-bottom:2px solid var(--blue);padding-bottom:3px}

/* hero */
.hero{height:330px;position:relative;background:radial-gradient(ellipse at 60% 45%,var(--hero-a),var(--hero-b) 75%)}
.hero-art{position:absolute;left:300px;top:22px;width:210px;height:290px;border-radius:12px;background:radial-gradient(circle at 50% 40%,rgba(120,180,240,.35),rgba(20,60,110,.05) 70%)}
.hero-copy{position:absolute;left:70px;top:125px;color:#fff}
.hero-copy h1{font-size:22px;font-weight:700;line-height:1.2;text-transform:uppercase}
.btn{display:inline-block;background:var(--blue);color:#fff;font-weight:700;text-transform:uppercase;font-size:8px;padding:7px 12px;border-radius:2px}
.hero-copy .btn{margin-top:14px}
.arrow{position:absolute;top:150px}
.arrow.left{left:8px}.arrow.right{right:8px}

/* login */
.login{display:flex;height:35px}
.login div{flex:1;display:flex;align-items:center;justify-content:center;gap:8px;color:#fff;font-weight:700;font-size:10px;text-transform:uppercase}
.login .student{background:var(--login-l)}
.login .professor{background:var(--blue)}

/* welcome */
.section-title{color:var(--blue);font-size:17px;font-weight:700;text-transform:uppercase}
.welcome{display:flex;gap:22px;padding:20px 70px 14px}
.welcome-text{flex:1}
.welcome-text p{color:var(--muted);font-size:7.5px;margin-top:6px}
.welcome-video{width:130px;height:78px;margin-top:22px;background:linear-gradient(135deg,#b9c4cc,#e6e9ec);position:relative}
.welcome-video svg{position:absolute;left:50px;top:24px}

/* classes */
.classes{padding:10px 70px 0}
.classes-head{display:flex;justify-content:space-between;align-items:center;border-bottom:1px solid var(--line);padding-bottom:6px}
.class-grid{display:flex;gap:8px;margin-top:10px}
.class-card{width:128px}
.class-photo{height:68px;background:linear-gradient(135deg,#c9d3da,#8ea2b3)}
.class-card h3{font-size:8px;font-weight:600;margin-top:6px;line-height:1.3}
.class-card .date{color:var(--blue);font-size:6.5px;margin-top:3px}
.class-card p{color:var(--muted);font-size:6.5px;line-height:1.4;margin-top:2px}

/* friend band */
.friend{margin-top:16px;background:linear-gradient(180deg,#1d86cc,#1670b0);height:82px;padding:14px 70px 0;text-align:center}
.friend h2{color:#fff;font-size:16px;font-weight:700;text-transform:uppercase}
.friend-form{display:flex;gap:8px;margin-top:12px}
.field{flex:1;background:#fff;height:17px;border-radius:2px;font-size:7px;color:#9aa3ab;text-align:left;padding:2px 7px}
.friend-form .submit{background:var(--green);color:#fff;font-size:7px;font-weight:600;padding:3px 8px;border-radius:2px}

/* testimonials */
.testimonials{padding:14px 70px 0;text-align:center;position:relative}
.testimonials .section-title{border-bottom:1px solid var(--line);padding-bottom:6px;text-align:left}
.quote{display:flex;gap:16px;align-items:center;margin-top:12px;text-align:left}
.avatar{width:58px;height:58px;border-radius:50%;background:linear-gradient(135deg,#d9dde0,#b7c0c7);flex:none}
.quote p{color:var(--muted);font-size:7.5px;font-style:italic}
.quote .who{color:var(--ink);font-weight:700;font-style:normal;margin-top:4px;font-size:7.5px}
.t-arrow{position:absolute;top:82px}
.t-arrow.left{left:24px}.t-arrow.right{right:24px}

/* footer */
.footer{position:absolute;left:0;top:933px;width:678px;height:205px;background:var(--foot);display:flex;gap:22px;padding:22px 40px 0 70px;color:var(--foot-text)}
.fcol h4{color:#fff;font-size:11px;font-weight:600;margin-bottom:8px}
.fcol p,.fcol li{font-size:6.5px;line-height:1.6}
.news{width:140px}
.news .headline{color:#fff;font-size:8px}
.tweets{width:130px}
.tweets li{list-style:none;padding-left:8px;position:relative;margin-bottom:6px}
.tweets li::before{content:"";position:absolute;left:0;top:4px;width:3px;height:3px;background:var(--foot-text)}
.links{width:80px}
.links ul{list-style:none}
.links li::before{content:"› "}
.newsletter{width:110px}
.nl-field{display:flex}
.nl-field span{flex:1;background:#fff;height:15px;color:#9aa3ab;font-size:6.5px;padding:2px 5px}
.nl-field b{width:15px;height:15px;background:#8f979e}
.newsletter h4.follow{margin-top:14px}
.social{display:flex;gap:8px}
.social i{width:10px;height:10px;background:#c9cfd4;display:block}
.bottom{position:absolute;left:0;top:1138px;width:678px;height:62px;background:var(--foot-2);padding:14px 70px;color:var(--foot-text);font-size:6.5px;display:flex;justify-content:space-between}
.bottom .legal span{margin-right:10px}
.bottom .dots{display:flex;gap:8px;align-items:flex-start}
.bottom .dots i{width:13px;height:13px;border:1px solid var(--foot-text);border-radius:50%;display:block}
</style>
</head>
<body>
<div class="site">
  <header class="topbar">
    <div class="brand"><span>RIPPLES</span><span class="brand-dot"></span></div>
    <ul class="nav">
      <li class="active">Home</li><li>Who we are</li><li>How it works</li><li>Classes</li><li>Clients</li><li>Support</li>
    </ul>
  </header>

  <section class="hero">
    <div class="hero-art" role="img" aria-label="Illustration of a glowing lightbulb above a cloud raining learning icons"></div>
    <div class="hero-copy">
      <h1>Aliquam vitae luctus<br>mollis mattis</h1>
      <span class="btn">Get started now</span>
    </div>
    <svg class="arrow left" width="10" height="20" viewBox="0 0 10 20"><path d="M8 2 2 10l6 8" fill="none" stroke="#fff" stroke-width="2"/></svg>
    <svg class="arrow right" width="10" height="20" viewBox="0 0 10 20"><path d="M2 2l6 8-6 8" fill="none" stroke="#fff" stroke-width="2"/></svg>
  </section>

  <div class="login">
    <div class="student"><svg width="10" height="10" viewBox="0 0 10 10"><path d="M1 5h6M5 2l3 3-3 3" stroke="#fff" stroke-width="1.5" fill="none"/></svg>Login as a student</div>
    <div class="professor"><svg width="10" height="10" viewBox="0 0 10 10"><circle cx="3.5" cy="5" r="2.5" fill="none" stroke="#fff" stroke-width="1.3"/><path d="M6 5h4M8.5 5v2" stroke="#fff" stroke-width="1.3"/></svg>Login as a professor</div>
  </div>

  <section class="welcome">
    <div class="welcome-text">
      <h2 class="section-title">Welcome to Ripples</h2>
      <p>Aenean magna tortor, facilisis eget eleifend nec, feugiat vitae velit. Vestibulum vitae ante in lectus tempus fringilla. Sed faucibus lorem vitae libero sollicitudin, et ullamcorper magna placerat. Vestibulum et tellus et massa fringilla mattis non in ipsum. Fusce egestas dui eros, sit amet malesuada magna placerat sed. Suspendisse potenti. Sed congue imperdiet cursus. Mauris iusto eleifend rutrum lectus, nec porta nisl varius eget.</p>
    </div>
    <div class="welcome-video" role="img" aria-label="Video still of a small study group around a table">
      <svg width="30" height="30" viewBox="0 0 30 30"><circle cx="15" cy="15" r="14" fill="rgba(0,0,0,.45)"/><path d="M12 9l9 6-9 6z" fill="#fff"/></svg>
    </div>
  </section>

  <section class="classes">
    <div class="classes-head">
      <h2 class="section-title">Classes</h2>
      <svg width="11" height="11" viewBox="0 0 11 11"><circle cx="5.5" cy="5.5" r="4.5" fill="none" stroke="#1b8fd6" stroke-width="1.5"/><circle cx="5.5" cy="5.5" r="1.5" fill="#1b8fd6"/></svg>
    </div>
    <div class="class-grid">
      <article class="class-card"><div class="class-photo" role="img" aria-label="Photo of students in a lecture"></div><h3>Sed volutpat augue vel libero molestie massa.</h3><div class="date">Dec 16, 2014</div><p>Donec lorem turpis, commodo ut nisl et, porta mattis quam. Nam dapibus enim nisi neque.</p></article>
      <article class="class-card"><div class="class-photo" role="img" aria-label="Photo of a learner at a laptop"></div><h3>Sed volutpat augue vel libero molestie massa.</h3><div class="date">Dec 16, 2014</div><p>Donec lorem turpis, commodo ut nisl et, porta mattis quam. Nam dapibus enim nisi neque.</p></article>
      <article class="class-card"><div class="class-photo" role="img" aria-label="Photo of a group working together"></div><h3>Sed volutpat augue vel libero molestie massa.</h3><div class="date">Dec 16, 2014</div><p>Donec lorem turpis, commodo ut nisl et, porta mattis quam. Nam dapibus enim nisi neque.</p></article>
      <article class="class-card"><div class="class-photo" role="img" aria-label="Photo of a tutor with a student"></div><h3>Sed volutpat augue vel libero molestie massa.</h3><div class="date">Dec 16, 2014</div><p>Donec lorem turpis, commodo ut nisl et, porta mattis quam. Nam dapibus enim nisi neque.</p></article>
    </div>
  </section>

  <section class="friend">
    <h2>Be a friend instrictor</h2>
    <div class="friend-form">
      <span class="field">Name</span><span class="field">E-mail</span><span class="field">Password</span><span class="submit">Get Started</span>
    </div>
  </section>

  <section class="testimonials">
    <h2 class="section-title">Testimonials</h2>
    <div class="quote">
      <div class="avatar" role="img" aria-label="Portrait of a smiling student"></div>
      <div>
        <p>" Nam a malesuada lorem. Duis sodales et libero nec pharetra. Vestibulum et malesuada libero, id suscipit turpis. Mauris in facilisis ante, vitae lobortis felis mollis nec. Sed sodales enim, luctus ac mauris id, accumsan dapibus sem. Nullam ultrices tempor tellus et ultrices."</p>
        <p class="who">Mara Dell, City</p>
      </div>
    </div>
    <svg class="t-arrow left" width="8" height="14" viewBox="0 0 8 14"><path d="M6 1 1 7l5 6" fill="none" stroke="#9aa3ab" stroke-width="1.5"/></svg>
    <svg class="t-arrow right" width="8" height="14" viewBox="0 0 8 14"><path d="M2 1l5 6-5 6" fill="none" stroke="#9aa3ab" stroke-width="1.5"/></svg>
  </section>

  <footer class="footer">
    <div class="fcol news">
      <h4>Latest News</h4>
      <p class="headline">Sed nec enim tempus</p>
      <p>Aliquam sit sed at, nibh sodales lacus semper. Cras condimentum est ligula eget dictum.</p>
      <p>Dec 16, 2014</p>
    </div>
    <div class="fcol tweets">
      <h4>Latest Tweet's</h4>
      <ul>
        <li>Praesent convallis placerat lectus, quis interdum felis feugiat at.</li>
        <li>Mauris ac purus consectetur cursus blandit malesuada.</li>
        <li>Nam dapibus enim nisi, sit amet pulvinar justo.</li>
      </ul>
    </div>
    <div class="fcol links">
      <h4>Quick Links</h4>
      <ul><li>Home</li><li>Who we are</li><li>How it works</li><li>Classes</li><li>Clients</li><li>Support</li></ul>
    </div>
    <div class="fcol newsletter">
      <h4>Newsletter</h4>
      <div class="nl-field"><span>E-mail</span><b></b></div>
      <h4 class="follow">Follow us on</h4>
      <div class="social"><i></i><i></i><i></i><i></i></div>
    </div>
  </footer>
  <div class="bottom">
    <div class="legal"><p>Copyright © 2014 · Ripples. All Rights Reserved.</p><p><span>Disclaimer</span><span>Support</span><span>Privacy Policy</span><span>Terms of use</span></p></div>
    <div class="dots"><i></i><i></i></div>
  </div>
</div>
</body>
</html>
```